Postcard Design

Income tax servicesOver 20 years experienceBusiness and Personal Tax ReturnsAll State ReturnsFree Electronic FilingI would like a simple map showing how to get to my house.reasons to use a tax preparerYou don’t have to keep up with the many tax law changes or understand complicated tax law.Your time is worth money – add up the hours you would spend doing it yourself and calculate what that’s worth.A tax program in a box cannot represent you in an audit.A tax professional can answer your questions to help you make smarter tax-saving decisions.It gives you peace of mind knowing that a professional is taking care of it.It can save you money – if your tax preparer finds even one significant deduction or tax credit you may have missed, it can easily cover the cost to have them prepared.Going to be targeting the area within 2 square miles of my home office so would like to promote proximity to the possible clients
Electronic

```html
<!DOCTYPE html>
<html lang="en">
<head>
<meta charset="utf-8">
<title>Income Tax Services Postcard</title>
<link rel="stylesheet" href="https://fonts.googleapis.com/css2?family=Fjalla+One&family=Open+Sans:wght@300;400;600;700&display=swap">
<style>
  :root {
    --stage: #3a3330;
    --blue: #1a6fc0;
    --blue-deep: #134f9c;
    --blue-light: #2c8ad8;
    --orange: #f0771d;
    --gold: #ffcf1a;
    --white: #ffffff;
    --ink: #3c3c3c;
    --pill: #e9e9ea;
    --stamp: #d7d7d8;
  }
  * { box-sizing: border-box; margin: 0; padding: 0; }
  html, body { width: 874px; height: 1200px; overflow: hidden; }
  body { background: var(--stage); position: relative; font-family: "Open Sans", sans-serif; }

  .card { position: absolute; left: 73px; width: 725px; height: 517px; overflow: hidden; box-shadow: 0 4px 14px rgba(0,0,0,.45); }
  .card--front { top: 66px; background: #1b1b1d; }
  .card--back { top: 626px; background: var(--white); }

  /* front */
  .front-photo { position: absolute; inset: 0; background:
      radial-gradient(ellipse at 22% 70%, #c48c6a 0%, #8a5a40 18%, transparent 40%),
      radial-gradient(ellipse at 70% 90%, #d9d9d9 0%, #9a9a9a 25%, transparent 50%),
      linear-gradient(180deg, #202022 0%, #141416 60%, #2a2a2c 100%); }
  .front-header { position: absolute; left: 0; top: 0; width: 725px; height: 200px; }
  .front-title { position: absolute; left: 29px; top: 18px; font-family: "Fjalla One", sans-serif; font-size: 47px; color: var(--white); letter-spacing: .5px; line-height: 1.2; }
  .front-subtitle { position: absolute; left: 29px; top: 76px; font-family: "Fjalla One", sans-serif; font-size: 25px; color: var(--white); line-height: 1.2; }
  .badge { position: absolute; left: 524px; top: 25px; width: 130px; height: 130px; }
  .feature { position: absolute; right: 46px; font-family: "Fjalla One", sans-serif; font-size: 35px; color: var(--gold); line-height: 1; display: flex; align-items: center; gap: 14px; text-shadow: 0 2px 3px rgba(0,0,0,.6); }
  .feature svg { width: 34px; height: 34px; }
  .feature--states { top: 194px; }
  .feature--efile { top: 242px; }
  .front-bar { position: absolute; left: 0; top: 477px; width: 725px; height: 40px; background: var(--blue); display: flex; align-items: center; color: var(--white); }
  .front-bar .web { position: absolute; left: 269px; font-size: 19px; font-weight: 700; }
  .front-bar .divider { position: absolute; left: 461px; top: 8px; width: 2px; height: 24px; background: var(--gold); }
  .front-bar .contact { position: absolute; left: 478px; font-family: "Fjalla One", sans-serif; font-size: 17px; }
  .front-bar .contact b { font-weight: 400; font-size: 24px; }
  .brand-box { position: absolute; left: 23px; top: 432px; width: 210px; height: 72px; background: var(--white); border-radius: 3px; text-align: center; padding-top: 9px; }
  .brand-name { display: inline-flex; align-items: center; gap: 8px; font-family: "Open Sans", sans-serif; font-weight: 700; font-size: 24px; color: #111; }
  .brand-name i { width: 14px; height: 14px; border-radius: 50%; background: #111; display: inline-block; }
  .brand-tag { font-size: 9px; color: #111; margin-top: 6px; }

  /* back */
  .reasons-title { position: absolute; left: 23px; top: 18px; font-family: "Fjalla One", sans-serif; font-size: 26px; color: var(--blue); line-height: 1.3; }
  .reasons { list-style: none; }
  .reason { position: absolute; left: 0; width: 361px; background: var(--pill); border-radius: 0 26px 26px 0; padding: 0 26px 0 42px; display: flex; align-items: center; font-size: 13px; font-weight: 300; color: var(--ink); line-height: 17.5px; text-align: justify; }
  .reason::before { content: ""; position: absolute; left: 22px; top: 10px; width: 13px; height: 13px; border-radius: 50%; background: radial-gradient(circle at 35% 30%, #8cc8ff, var(--blue) 60%, #0d3f80); }
  .illustration { position: absolute; left: 347px; top: 18px; width: 148px; height: 115px; border-radius: 50% 40% 30% 50%; background: linear-gradient(120deg, #f4f4f4 0%, #e0e0e0 50%, #3bb4d0 100%); }
  .stamp-box { position: absolute; left: 621px; top: 17px; width: 73px; height: 80px; background: var(--stamp); }
  .map { position: absolute; left: 414px; top: 133px; width: 276px; height: 157px; border-radius: 8px; background: linear-gradient(135deg, #e8e4d4 0%, #dfe8c9 40%, #f1ead0 70%, #cfdde8 100%); box-shadow: 0 1px 3px rgba(0,0,0,.3); }
  .address-box { position: absolute; left: 414px; top: 306px; width: 276px; height: 142px; border: 2px solid #d6d6d6; border-radius: 6px; box-shadow: 0 1px 3px rgba(0,0,0,.2); }
  .address-box span { position: absolute; left: 12px; right: 12px; height: 1px; background: #bdbdbd; }
  .back-bar { position: absolute; left: 0; top: 466px; width: 725px; height: 51px; background: var(--blue-deep); border-top: 4px solid var(--orange); color: var(--white); }
  .back-bar .name { position: absolute; left: 25px; top: 6px; font-family: "Fjalla One", sans-serif; font-size: 24px; }
  .back-bar .email { position: absolute; left: 282px; top: 10px; font-size: 17px; font-weight: 700; }
  .back-bar .contact { position: absolute; left: 517px; top: 9px; font-family: "Fjalla One", sans-serif; font-size: 15px; }
  .back-bar .contact b { font-weight: 400; font-size: 19px; }
  .back-bar .sep { position: absolute; top: 10px; width: 1px; height: 24px; background: rgba(255,255,255,.7); }
</style>
</head>
<body>

<section class="card card--front">
  <div class="front-photo" role="img" aria-label="Photo of a hand signing tax documents with a fountain pen"></div>

  <svg class="front-header" viewBox="0 0 725 200" aria-hidden="true">
    <defs>
      <linearGradient id="headerBlue" x1="0" y1="0" x2="1" y2="1">
        <stop offset="0" stop-color="#1d63b4"/>
        <stop offset="1" stop-color="#2a86d2"/>
      </linearGradient>
    </defs>
    <path d="M0 140 C60 200 180 185 290 150 C430 105 560 115 725 140 L725 170 C580 125 440 130 300 165 C170 205 60 205 0 155 Z" fill="var(--orange)"/>
    <path d="M0 0 H725 V140 C560 112 430 100 290 145 C180 180 70 195 0 130 Z" fill="url(#headerBlue)"/>
  </svg>

  <h1 class="front-title">Income Tax Services</h1>
  <p class="front-subtitle">Business and Personal Tax Returns</p>

  <svg class="badge" viewBox="0 0 130 130" aria-label="20 years experience">
    <defs>
      <radialGradient id="badgeOrange" cx="0.4" cy="0.35" r="0.7">
        <stop offset="0" stop-color="#ffd24a"/>
        <stop offset="1" stop-color="#f08a12"/>
      </radialGradient>
      <path id="ringTop" d="M20 65 A45 45 0 0 1 110 65"/>
      <path id="ringBottom" d="M16 65 A49 49 0 0 0 114 65"/>
    </defs>
    <circle cx="65" cy="65" r="64" fill="#fff"/>
    <circle cx="65" cy="65" r="60" fill="#fff" stroke="#1a1a1a" stroke-width="1"/>
    <circle cx="65" cy="65" r="38" fill="url(#badgeOrange)" stroke="#1a1a1a" stroke-width="1"/>
    <text font-family="Fjalla One, sans-serif" font-size="16" fill="#1a1a1a" letter-spacing="1"><textPath href="#ringTop" startOffset="50%" text-anchor="middle">EXPERIENCE</textPath></text>
    <text font-family="Fjalla One, sans-serif" font-size="16" fill="#1a1a1a" letter-spacing="1"><textPath href="#ringBottom" startOffset="50%" text-anchor="middle" dominant-baseline="hanging">EXPERIENCE</textPath></text>
    <text x="65" y="72" text-anchor="middle" font-family="Fjalla One, sans-serif" font-size="42" fill="#1a1a1a">20</text>
    <text x="65" y="90" text-anchor="middle" font-family="Fjalla One, sans-serif" font-size="15" fill="#1a1a1a">years</text>
    <text x="11" y="70" font-size="9" fill="#1a1a1a">★</text>
    <text x="112" y="70" font-size="9" fill="#1a1a1a">★</text>
  </svg>

  <p class="feature feature--states">All State Returns
    <svg viewBox="0 0 34 34" aria-hidden="true"><path d="M4 18 L13 27 L30 5" fill="none" stroke="#fff" stroke-width="5" stroke-linecap="round" stroke-linejoin="round"/></svg>
  </p>
  <p class="feature feature--efile">Free Electronic Filing
    <svg viewBox="0 0 34 34" aria-hidden="true"><path d="M4 18 L13 27 L30 5" fill="none" stroke="#fff" stroke-width="5" stroke-linecap="round" stroke-linejoin="round"/></svg>
  </p>

  <div class="front-bar">
    <span class="web">www.website.com</span>
    <span class="divider"></span>
    <span class="contact">Contact Us: <b>000 000 0000</b></span>
  </div>

  <div class="brand-box">
    <div class="brand-name"><i></i>Ledgerline</div>
    <p class="brand-tag">Ledgerline. Careful Returns, Every Year.</p>
  </div>
</section>

<section class="card card--back">
  <h2 class="reasons-title">Reasons to use a tax preparer</h2>
  <ul class="reasons">
    <li class="reason" style="top:62px;height:42px;">You don’t have to keep up with the many tax law changes or understand complicated tax law.</li>
    <li class="reason" style="top:107px;height:57px;">Your time is worth money – add up the hours you would spend doing it yourself and calculate what that’s worth.</li>
    <li class="reason" style="top:167px;height:40px;">A tax program in a box cannot represent you in an audit.</li>
    <li class="reason" style="top:212px;height:40px;">$$ tax professional can answer your questions to help you make smarter tax-saving decisions.</li>
    <li class="reason" style="top:257px;height:40px;">It gives you peace of mind knowing that a professional is taking care of it.</li>
    <li class="reason" style="top:302px;height:76px;">It can save you money – if your tax preparer finds even one significant deduction or tax credit you may have missed, it can easily cover the cost to have them prepared.</li>
    <li class="reason" style="top:383px;height:57px;">Going to be targeting the area within 2 square miles of my home office so would like to promote proximity to the possible clients</li>
  </ul>

  <div class="illustration" role="img" aria-label="Illustration of a woman drawing a clock labelled time for taxes"></div>
  <div class="stamp-box" aria-hidden="true"></div>
  <div class="map" role="img" aria-label="Street map showing the route to the home office"></div>

  <div class="address-box" aria-label="Mailing address area">
    <span style="top:48px;"></span>
    <span style="top:85px;"></span>
    <span style="top:122px;"></span>
  </div>

  <div class="back-bar">
    <span class="name">INCOME TAX SERVICES</span>
    <span class="sep" style="left:268px;"></span>
    <span class="email">email: info@website.com</span>
    <span class="sep" style="left:503px;"></span>
    <span class="contact">Contact Us: <b>000 000 0000</b></span>
  </div>
</section>

</body>
</html>
```